Design a For Sale sign board and Direction Sign Board.
Attached is an example of what i am thinking but am happy to look at any options.
Colours are to be ""bright Orange"on white and in reverse as well.

Logo id Fairbrook & Co Real Estate.

```html
<!DOCTYPE html>
<html lang="en">
<head>
<meta charset="utf-8">
<title>Fairbrook &amp; Co Real Estate – Sign Boards</title>
<link href="https://fonts.googleapis.com/css2?family=Montserrat:wght@700;800&family=Oswald:wght@200&display=swap" rel="stylesheet">
<style>
  :root {
    --brand-orange: #e14f24;
    --ink: #0d0d0d;
    --paper: #ffffff;
  }
  html, body {
    margin: 0;
    padding: 0;
    width: 986px;
    height: 1200px;
    overflow: hidden;
    background: var(--paper);
  }
  .canvas {
    position: relative;
    width: 986px;
    height: 1200px;
  }
  .sign-board {
    position: absolute;
    left: 169px;
    width: 652px;
    height: 489px;
    filter: drop-shadow(0 8px 14px rgba(0,0,0,0.28));
  }
  .sign-board--standard { top: 64px; }
  .sign-board--direction { top: 675px; }
  .fill-orange { fill: var(--brand-orange); }
  .fill-white { fill: var(--paper); }
  .fill-ink { fill: var(--ink); }
  .logo-frame {
    fill: none;
    stroke: var(--paper);
    stroke-width: 4.5;
  }
  .brand-name {
    font-family: "Montserrat", sans-serif;
    font-weight: 800;
    font-size: 62px;
    fill: var(--paper);
  }
  .brand-tagline {
    font-family: "Montserrat", sans-serif;
    font-weight: 700;
    font-size: 40px;
    fill: var(--paper);
  }
  .brand-tagline--light {
    font-family: "Oswald", sans-serif;
    font-weight: 200;
    font-size: 50px;
  }
  .agent-name {
    font-family: "Montserrat", sans-serif;
    font-weight: 700;
    font-size: 94px;
    fill: var(--brand-orange);
  }
  .agent-phone {
    font-family: "Montserrat", sans-serif;
    font-weight: 800;
    font-size: 60px;
    fill: var(--ink);
  }
  .agent-phone--arrow {
    font-size: 37px;
    fill: var(--brand-orange);
    stroke: var(--paper);
    stroke-width: 4;
    paint-order: stroke;
    stroke-linejoin: round;
  }
  .speed-line {
    stroke: var(--ink);
    stroke-width: 4.5;
  }
</style>
</head>
<body>
<main class="canvas">

  <!-- Standard sign board -->
  <svg class="sign-board sign-board--standard" viewBox="0 0 652 489" aria-label="Fairbrook &amp; Co Real Estate agent sign, Dana Hollis">
    <rect class="fill-white" x="0" y="0" width="652" height="489"/>
    <rect class="fill-orange" x="0" y="0" width="652" height="260"/>
    <path class="logo-frame" d="M186 196 H27 V52 H625 V196 H466"/>
    <text class="brand-name" x="50" y="152" textLength="554" lengthAdjust="spacingAndGlyphs">FAIRBROOK &amp; CO</text>
    <text class="brand-tagline" x="326" y="206" text-anchor="middle">REAL ESTATE</text>

    <text class="agent-name" x="18" y="361" textLength="611" lengthAdjust="spacingAndGlyphs">DANA HOLLIS</text>

    <g class="speed-lines">
      <line class="speed-line" x1="18" y1="393" x2="97" y2="393"/>
      <line class="speed-line" x1="38" y1="407" x2="97" y2="407"/>
      <line class="speed-line" x1="58" y1="423" x2="97" y2="423"/>
      <line class="speed-line" x1="545" y1="393" x2="625" y2="393"/>
      <line class="speed-line" x1="545" y1="407" x2="605" y2="407"/>
      <line class="speed-line" x1="545" y1="423" x2="585" y2="423"/>
    </g>
    <text class="agent-phone" x="326" y="431" text-anchor="middle" textLength="410" lengthAdjust="spacingAndGlyphs">0400 123 456</text>

    <rect class="fill-ink" x="0" y="461" width="652" height="12"/>
    <rect class="fill-orange" x="0" y="477" width="652" height="12"/>
  </svg>

  <!-- Direction sign board -->
  <svg class="sign-board sign-board--direction" viewBox="0 0 652 489" aria-label="Fairbrook &amp; Co Real Estate direction sign, Dana Hollis">
    <rect class="fill-white" x="0" y="0" width="652" height="489"/>
    <rect class="fill-orange" x="0" y="0" width="652" height="281"/>
    <path class="logo-frame" d="M186 196 H27 V62 H625 V196 H466"/>
    <text class="brand-name" x="50" y="153" textLength="554" lengthAdjust="spacingAndGlyphs">FAIRBROOK &amp; CO</text>
    <text class="brand-tagline brand-tagline--light" x="326" y="208" text-anchor="middle">REAL ESTATE</text>

    <text class="agent-name" x="37" y="373" textLength="575" lengthAdjust="spacingAndGlyphs">DANA HOLLIS</text>

    <g class="direction-arrow">
      <polygon class="fill-ink" points="37,420 70,390 507,390 477,420 507,449 70,449"/>
      <polygon class="fill-ink" points="515,390 535,390 505,420 535,449 515,449 485,420"/>
      <polygon class="fill-ink" points="543,390 563,390 533,420 563,449 543,449 513,420"/>
      <polygon class="fill-ink" points="571,390 591,390 561,420 591,449 571,449 541,420"/>
    </g>
    <text class="agent-phone agent-phone--arrow" x="291" y="432" text-anchor="middle" textLength="270" lengthAdjust="spacingAndGlyphs">0400 123 456</text>

    <rect class="fill-ink" x="0" y="463" width="652" height="11"/>
    <rect class="fill-orange" x="0" y="478" width="652" height="11"/>
  </svg>

</main>
</body>
</html>
```